Pharmacy

Two sided postcard. Pictures on one side. Description on the other. We design and build pharmacies. pictures are some of our finished work. You can use as many pictures as you like not necessary to use all of them. Size of card should be 5"x7". See my website at display@brightfieldfixtures.com for more inspiration. I include the back of one card that I used recently. Both sids need design input. Feel free to contact me with questions.
Requirements
Must have
- Must be a two sided postcard
Nice to have
- I am sending a design of a sleek type postcard that I saw online as an example.
- https://lnk.example-pics.net/images/q7KmRz
- I am looking for something modern.
- Not limited to colors on my website.

```html
<!DOCTYPE html>
<html lang="en">
<head>
<meta charset="utf-8">
<title>Brightfield Showcase &amp; Store Fixture Co. Inc. – Postcard</title>
<link rel="stylesheet" href="https://fonts.googleapis.com/css2?family=Libre+Baskerville:wght@700&family=Open+Sans:wght@400;600;700&display=swap">
<style>
  :root {
    --maroon: #7d0f10;
    --cream: #fffbe2;
    --blush: #ecdad4;
    --ink: #1d1a17;
    --white: #ffffff;
    --stage: #e6e6e6;
    --rule: #777;
  }
  * { box-sizing: border-box; margin: 0; padding: 0; }
  html, body { width: 880px; height: 1200px; overflow: hidden; }
  body { background: var(--stage); position: relative; font-family: "Open Sans", Arial, sans-serif; color: var(--ink); }

  .card { position: absolute; left: 113px; width: 654px; height: 467px; overflow: hidden; }

  /* Front */
  .front { top: 93px; background: var(--cream); }
  .front-title {
    height: 60px; display: flex; align-items: center; justify-content: center;
    font-family: "Libre Baskerville", Georgia, serif; font-weight: 700;
    font-size: 22px; color: var(--maroon); letter-spacing: .2px; white-space: nowrap;
  }
  .gallery { display: block; width: 654px; height: 327px; background: var(--maroon); }
  .front-cta {
    height: 80px; display: flex; align-items: center; justify-content: center; gap: 20px;
    color: var(--maroon); font-weight: 700; white-space: nowrap;
  }
  .front-cta .label { font-size: 40px; letter-spacing: .3px; }
  .front-cta .number { font-size: 49px; letter-spacing: .5px; }
  .front-cta svg { width: 50px; height: 50px; flex: none; }

  /* Back */
  .back { top: 652px; background: var(--white); }
  .message { position: absolute; left: 0; top: 0; width: 327px; height: 467px; background: var(--cream); }
  .back-title {
    height: 94px; background: var(--maroon); color: var(--white);
    font-family: "Libre Baskerville", Georgia, serif; font-weight: 700;
    font-size: 23px; line-height: 27px; text-align: center; padding-top: 20px;
  }
  .values {
    margin-top: 13px; height: 41px; background: var(--blush);
    display: flex; align-items: center; justify-content: center; gap: 14px;
    font-family: "Libre Baskerville", Georgia, serif; font-weight: 700; font-size: 13px; color: var(--maroon);
    white-space: nowrap;
  }
  .values span { display: flex; align-items: center; gap: 6px; }
  .values svg { width: 15px; height: 15px; }
  .about {
    padding: 16px 16px 0 19px; font-size: 12.6px; line-height: 17.7px; text-align: justify; height: 162px;
  }
  .back-cta { height: 72px; background: var(--maroon); position: relative; }
  .back-cta .frame {
    position: absolute; left: 18px; top: 16px; width: 302px; height: 50px;
    border: 2px solid var(--white); border-radius: 9px;
    display: flex; align-items: center; gap: 10px; padding-left: 6px; color: var(--white);
    white-space: nowrap;
  }
  .back-cta .label {
    position: absolute; left: 10px; top: -16px; background: var(--maroon); padding: 0 6px;
    font-size: 21px; font-weight: 600; line-height: 26px;
  }
  .back-cta .number { font-size: 34px; font-weight: 700; letter-spacing: .3px; line-height: 40px; margin-top: 4px; }
  .back-cta svg { width: 38px; height: 38px; flex: none; margin-top: 2px; }
  .contacts { padding: 16px 0 0 20px; font-size: 16.5px; line-height: 24px; white-space: nowrap; }
  .contacts li { list-style: none; display: flex; align-items: center; gap: 6px; }
  .contacts svg { width: 14px; height: 14px; }

  .mailing { position: absolute; left: 410px; top: 26px; font-size: 10.5px; line-height: 14.4px; font-style: normal; }
  .stamp { position: absolute; left: 543px; top: 22px; width: 94px; height: 94px; border: 1px solid var(--rule); }
  .address-line { position: absolute; left: 455px; width: 182px; border-top: 1px solid var(--rule); }
  .line-1 { top: 256px; } .line-2 { top: 283px; } .line-3 { top: 310px; } .line-4 { top: 337px; }
</style>
</head>
<body>

<section class="card front">
  <h1 class="front-title">Brightfield Showcase &amp; Store Fixture Co. Inc.</h1>

  <svg class="gallery" viewBox="0 0 654 327">
    <defs>
      <linearGradient id="tone-warm" x1="0" y1="0" x2="1" y2="1">
        <stop offset="0" stop-color="#c9a27a"/><stop offset="1" stop-color="#5e4030"/>
      </linearGradient>
      <linearGradient id="tone-bright" x1="0" y1="0" x2="1" y2="1">
        <stop offset="0" stop-color="#e9e4dd"/><stop offset="1" stop-color="#b88a6a"/>
      </linearGradient>
      <linearGradient id="tone-cool" x1="0" y1="0" x2="1" y2="1">
        <stop offset="0" stop-color="#d7dbe0"/><stop offset="1" stop-color="#6f7178"/>
      </linearGradient>
      <linearGradient id="tone-dark" x1="0" y1="0" x2="1" y2="1">
        <stop offset="0" stop-color="#4a3a30"/><stop offset="1" stop-color="#e8e6e2"/>
      </linearGradient>
    </defs>
    <g stroke="#ffffff" stroke-width="2">
      <polygon role="img" aria-label="Photo: pharmacy cosmetics counter with glass display cases" fill="url(#tone-warm)" points="35,16 234,16 199,156 10,156"/>
      <polygon role="img" aria-label="Photo: white wall shelving stocked with skincare products" fill="url(#tone-bright)" points="242,16 444,16 409,156 215,156"/>
      <polygon role="img" aria-label="Photo: pharmacy aisle with gondola fixtures and product displays" fill="url(#tone-cool)" points="455,16 644,16 609,156 421,156"/>
      <polygon role="img" aria-label="Photo: white beauty counter in a dark-shelved boutique pharmacy" fill="url(#tone-dark)" points="35,172 234,172 199,312 10,312"/>
      <polygon role="img" aria-label="Photo: curved wooden end-cap shelving with health products" fill="url(#tone-bright)" points="242,172 444,172 409,312 215,312"/>
      <polygon role="img" aria-label="Photo: pharmacy service counter with pendant lights and mortar and pestle" fill="url(#tone-warm)" points="455,172 644,172 609,312 421,312"/>
    </g>
  </svg>

  <div class="front-cta">
    <span class="label">Call Now</span>
    <svg viewBox="0 0 54 54" aria-hidden="true">
      <path d="M12 46 A23 23 0 1 1 30 49.8" fill="none" stroke="#7d0f10" stroke-width="3.5" stroke-linecap="round"/>
      <path d="M19 14 l6 -2 l4 9 l-4 3 q3 7 9 10 l3 -4 l9 4 l-2 6 q-2 3 -6 2 q-14 -5 -20 -20 q-1 -5 1 -8z" fill="none" stroke="#7d0f10" stroke-width="3.2" stroke-linejoin="round"/>
    </svg>
    <span class="number">555 214 0387</span>
  </div>
</section>

<section class="card back">
  <div class="message">
    <h2 class="back-title">Brightfield Showcase &amp;<br>Store Fixture Co. Inc.</h2>

    <div class="values">
      <span><svg viewBox="0 0 15 15" aria-hidden="true"><path d="M1 8 l4 5 l9 -12" fill="none" stroke="#7d0f10" stroke-width="2.4"/></svg>Quality</span>
      <span><svg viewBox="0 0 15 15" aria-hidden="true"><path d="M1 8 l4 5 l9 -12" fill="none" stroke="#7d0f10" stroke-width="2.4"/></svg>Experience</span>
      <span><svg viewBox="0 0 15 15" aria-hidden="true"><path d="M1 8 l4 5 l9 -12" fill="none" stroke="#7d0f10" stroke-width="2.4"/></svg>Innovation</span>
    </div>

    <p class="about">Family owned and operated for three generations -Brightfield Showcase &amp; Store Fixture Co. Inc is the oldest store fixture company in New Jersey. As designers &amp; Manufacturers we can save you hours of time and money. Our level of experience will be evident from the outset and you will be pleased that you found us.</p>

    <div class="back-cta">
      <div class="frame">
        <span class="label">Call Now</span>
        <svg viewBox="0 0 54 54" aria-hidden="true">
          <path d="M12 46 A23 23 0 1 1 30 49.8" fill="none" stroke="#ffffff" stroke-width="3.5" stroke-linecap="round"/>
          <path d="M19 14 l6 -2 l4 9 l-4 3 q3 7 9 10 l3 -4 l9 4 l-2 6 q-2 3 -6 2 q-14 -5 -20 -20 q-1 -5 1 -8z" fill="none" stroke="#ffffff" stroke-width="3.2" stroke-linejoin="round"/>
        </svg>
        <span class="number">555 214 0387</span>
      </div>
    </div>

    <ul class="contacts">
      <li><svg viewBox="0 0 14 14" aria-hidden="true"><rect x="1" y="3" width="12" height="8" fill="none" stroke="#7d0f10" stroke-width="1.2"/><path d="M1 3 l6 5 l6 -5" fill="none" stroke="#7d0f10" stroke-width="1.2"/></svg>display@brightfieldfixtures.com</li>
      <li><svg viewBox="0 0 14 14" aria-hidden="true"><g fill="none" stroke="#7d0f10" stroke-width="1.1"><circle cx="7" cy="7" r="6"/><ellipse cx="7" cy="7" rx="2.6" ry="6"/><path d="M1 7 h12 M2 4 h10 M2 10 h10"/></g></svg>www.brightfieldfixtures.com</li>
    </ul>
  </div>

  <address class="mailing">
    Brightfield Showcase &amp;<br>Store Fixture Co. Inc.<br>PO Box 318<br>Alder Falls NJ 07012
  </address>
  <div class="stamp"></div>
  <div class="address-line line-1"></div>
  <div class="address-line line-2"></div>
  <div class="address-line line-3"></div>
  <div class="address-line line-4"></div>
</section>

</body>
</html>
```